Book cover for a book about time management for women

We need a book cover for a book about time management for women written by a woman. Even though the book has a provocative title "Calendar candy" based on the seminars the author holds for women seeking the change in their life, it has nothing to do with the words themselves. The subtitle is "Keep each morning in your grip. A bold guide on daily rhythm for ladies today"

Preferred fonts (not necessarily):
Plus Jakarta Sans
Tiempos Headline

Preferred colours (not necessarily):
- orange
- pastel "highlighters"

We look for a simple/clean design that catches the attention of the women without too many graphic elements.

Target Market(s)

Women that want to change and organise their life

Industry/Entity Type

productivity, marketing, work-life balance

Font styles to use
Other font styles liked:
• Plus Jakarta Sans, Tiempos Headline

Colors
F0912C
F2A743
F7CA91
FBE8D2
FDF5EE
A7469A
B969AE
D3A5CF
EDDBEB
F8F0F9

Requirements
Must have
• Famine feeling as the target audience are women with drive to better life
Should not have
• No explicit images or sexually motivated themes

```html
<!DOCTYPE html>
<html lang="en">
<head>
<meta charset="utf-8">
<title>Calendar Candy – Book Cover</title>
<link rel="stylesheet" href="https://fonts.googleapis.com/css2?family=Plus+Jakarta+Sans:wght@700;800&family=Alegreya:wght@400&display=swap">
<style>
  :root {
    --stage: #ff7430;
    --paper: #f6e3d4;
    --title-orange: #ff7532;
    --ink-purple: #4b1866;
    --deep-purple: #531870;
    --bright-purple: #8a30c4;
    --sun-light: #fca22f;
    --sun-deep: #ff6a0a;
    --art-top: #4a1560;
    --art-mid: #f39a2a;
    --art-base: #7a2a5e;
  }
  * { margin: 0; padding: 0; box-sizing: border-box; }
  html, body {
    width: 1200px;
    height: 1200px;
    overflow: hidden;
    background: var(--stage);
  }
  .canvas {
    position: relative;
    width: 1200px;
    height: 1200px;
    background: var(--stage);
  }
  .cover {
    position: absolute;
    left: 301px;
    top: 106px;
    width: 647px;
    height: 970px;
    background: var(--paper);
    overflow: hidden;
  }
  .cover-art {
    position: absolute;
    inset: 0;
    width: 647px;
    height: 970px;
  }
  .title {
    position: absolute;
    left: 50px;
    top: 18px;
    font-family: "Plus Jakarta Sans", sans-serif;
    font-weight: 800;
    color: var(--title-orange);
    line-height: 1;
  }
  .title-top {
    display: block;
    font-size: 70px;
    letter-spacing: 1px;
  }
  .title-main {
    display: block;
    font-size: 158px;
    letter-spacing: -3px;
    margin-top: -4px;
    margin-left: -6px;
  }
  .subtitle {
    position: absolute;
    left: 55px;
    top: 252px;
    font-family: "Alegreya", serif;
    font-size: 27px;
    line-height: 30px;
    color: var(--ink-purple);
  }
  .author {
    position: absolute;
    left: 0;
    right: 0;
    top: 795px;
    text-align: center;
    font-family: "Plus Jakarta Sans", sans-serif;
    font-weight: 800;
    color: var(--paper);
    line-height: 1;
  }
  .author-first {
    display: block;
    font-size: 46px;
    letter-spacing: -1px;
  }
  .author-last {
    display: block;
    font-size: 96px;
    letter-spacing: -3px;
    margin-top: 2px;
  }
</style>
</head>
<body>
<main class="canvas">
  <section class="cover">
    <svg class="cover-art" viewBox="0 0 647 970" xmlns="http://www.w3.org/2000/svg">
      <defs>
        <linearGradient id="sun-gradient" x1="0" y1="1" x2="1" y2="0">
          <stop offset="0" stop-color="var(--sun-deep)"/>
          <stop offset="1" stop-color="var(--sun-light)"/>
        </linearGradient>
        <linearGradient id="band-gradient" x1="0" y1="0" x2="0" y2="1">
          <stop offset="0" stop-color="var(--bright-purple)"/>
          <stop offset="0.7" stop-color="var(--deep-purple)"/>
        </linearGradient>
        <linearGradient id="art-gradient" x1="0" y1="0" x2="0" y2="1">
          <stop offset="0" stop-color="var(--art-top)"/>
          <stop offset="0.45" stop-color="#6a2060"/>
          <stop offset="0.7" stop-color="var(--art-mid)"/>
          <stop offset="1" stop-color="var(--art-base)"/>
        </linearGradient>
      </defs>
      <polygon class="purple-band" points="0,653 339,864 647,518 647,970 0,970" fill="url(#band-gradient)"/>
      <circle class="sun-disc" cx="339" cy="602" r="249" fill="url(#sun-gradient)"/>
      <path class="hero-illustration" role="img" aria-label="Illustration of a confident woman with voluminous dark curly hair, hoop earrings and an orange blouse, hands on hips"
            d="M140 970 L140 520 A199 199 0 0 1 538 520 L538 970 Z" fill="url(#art-gradient)"/>
    </svg>

    <h1 class="title">
      <span class="title-top">CALENDAR</span>
      <span class="title-main">CANDY</span>
    </h1>

    <p class="subtitle">Keep each morning in your grip.<br>A bold guide on daily rhythm for ladies today.</p>

    <p class="author">
      <span class="author-first">AUTHOR</span>
      <span class="author-last">NAME</span>
    </p>
  </section>
</main>
</body>
</html>
```